Website Design For Ecommerce Brand That Sells Personalized Wall Decor

We need a new website for our company Copper Lantern. Our current site is functioning through wordpress/woocomerce but we are not happy with the appearance. Our products really wow people when they receive them and we need your help making our website do the same!

Number of Pages Required

4 page

```html
<!DOCTYPE html>
<html lang="en">
<head>
<meta charset="utf-8">
<title>Copper Lantern — Personalized Wall Decor</title>
<link href="https://fonts.googleapis.com/css2?family=Poppins:wght@300;400;500;600&family=Roboto+Condensed:wght@400&display=swap" rel="stylesheet">
<style>
:root{
  --green:#6a9a5b;
  --green-dark:#5a8a4c;
  --mint:#e9efe6;
  --ink:#222;
  --muted:#555;
  --line:#e3e3e3;
  --black:#000;
  --white:#fff;
  --tab:#e7ece4;
  --grey-btn:#9a9a9a;
}
*{box-sizing:border-box;margin:0;padding:0}
html,body{width:1200px;height:3273px;overflow:hidden}
body{font-family:'Poppins',sans-serif;color:var(--ink);background:var(--white);position:relative}
.abs{position:absolute}
a{color:inherit;text-decoration:none}

/* top bar */
.topbar{left:0;top:0;width:1200px;height:35px;background:var(--mint)}
.topbar .mail{left:308px;top:8px;font-size:14px;color:#444;display:flex;align-items:center;gap:8px}
.topbar .links{left:778px;top:10px;font-size:12px;display:flex;gap:28px;color:#333}
.topbar .icons{left:1000px;top:6px;display:flex;gap:9px}
.ring{width:24px;height:24px;border:1.5px solid var(--green);border-radius:50%;display:flex;align-items:center;justify-content:center}

/* header */
.brand{left:142px;top:50px;width:132px;font-size:28px;font-weight:500;line-height:1;text-align:center;letter-spacing:1px}
.brand small{display:block;font-size:20px;letter-spacing:6px;margin-top:6px}
.brand-dot{left:190px;top:8px;width:38px;height:38px;border-radius:50%;background:#222}
.search{left:707px;top:68px;width:352px;height:41px;border:1px solid #ccc;display:flex;align-items:center;justify-content:space-between;padding:0 12px 0 18px;font-size:12px;color:#444}

/* nav */
.nav{left:0;top:125px;width:1200px;height:36px;background:var(--green)}
.nav ul{position:absolute;left:142px;top:0;height:36px;display:flex;align-items:center;list-style:none;color:var(--white);font-size:13px}
.nav li{padding:0 10px;border-left:1px solid rgba(255,255,255,.45)}
.nav li:first-child{padding-left:0;border-left:0;font-weight:600}

/* hero */
.hero{left:0;top:161px;width:1200px;height:486px;background:linear-gradient(100deg,#3a2a1e 0%,#4a3424 35%,#3b2b20 60%,#2e231b 100%)}
.hero-ornaments{left:210px;top:200px;width:390px;height:420px;background:radial-gradient(ellipse at center,rgba(214,188,150,.45),rgba(214,188,150,0) 70%)}
.hero-copy{left:695px;top:248px;color:var(--white)}
.hero-copy h1{font-family:'Roboto Condensed',sans-serif;font-weight:400;font-size:52px;line-height:1.05}
.hero-copy h2{font-weight:400;font-size:23px;margin-top:16px}
.hero-copy ul{list-style:none;font-size:21px;line-height:25.6px;margin-top:14px;font-weight:300}
.btn{display:inline-flex;align-items:center;justify-content:center;color:var(--white);background:var(--green)}
.hero-copy .btn{width:144px;height:46px;font-size:21px;margin-top:18px}

/* section titles */
.sec-title{left:0;width:1200px;text-align:center;font-size:38px;font-weight:400;letter-spacing:.5px}
.sec-rule{left:557px;width:86px;height:3px;background:var(--green)}

/* categories */
.cat{width:209px;height:168px;background:var(--white);box-shadow:0 0 10px rgba(0,0,0,.09);text-align:center}
.cat svg{position:absolute;left:77px;top:28px}
.cat .bar{position:absolute;left:87px;top:102px;width:36px;height:2px;background:var(--green)}
.cat span{position:absolute;left:0;top:114px;width:100%;font-size:14.5px;color:#333}

/* tabs */
.tab{top:1337px;height:29px;background:var(--tab);font-size:12px;color:#444;display:flex;align-items:center;justify-content:center}
.tab.on{background:var(--green);color:var(--white);font-size:14px;font-weight:500}

/* products */
.card{width:294px;height:318px;background:var(--white);box-shadow:0 0 10px rgba(0,0,0,.09)}
.card .ph{position:absolute;left:7px;top:8px;width:281px;height:183px}
.card h3{position:absolute;left:10px;top:208px;width:274px;text-align:center;font-size:13px;font-weight:500;line-height:19px}
.card .acts{position:absolute;left:8px;top:264px;display:flex;gap:7px}
.card .acts .ring{width:29px;height:29px}
.card .price{position:absolute;right:9px;top:270px;font-size:14.5px;color:var(--green);font-weight:500}
.badge{position:absolute;left:9px;top:10px;width:34px;height:34px;border-radius:50%;background:#f08a1c;color:var(--white);font-size:9px;font-weight:600;display:flex;align-items:center;justify-content:center}

/* coupon */
.coupon{left:299px;top:2232px;width:630px;height:113px;background:var(--white);border-radius:0 56px 56px 0;box-shadow:0 18px 18px -12px rgba(0,0,0,.25)}
.coupon-dark{left:299px;top:2232px}
.coupon-text{left:326px;top:2250px;color:var(--white);font-weight:600;line-height:1}
.coupon-text .get{font-size:20px}
.coupon-text .pct{font-size:52px;font-weight:300;color:var(--green)}
.coupon-text .off{font-size:20px}
.coupon-text .sub{font-size:14px;font-weight:500;margin-top:2px;margin-left:14px}
.field{top:2253px;height:31px;border:1px solid #ddd;font-size:11px;color:#555;display:flex;align-items:center;gap:6px;padding-left:10px}
.coupon .btn{}

/* about */
.about{left:0;top:2415px;width:1200px;height:409px;background:linear-gradient(180deg,#6c9c5d,#6a995a);color:var(--white);text-align:center}
.about h2{position:absolute;left:0;top:66px;width:100%;font-size:43px;font-weight:400}
.about p{position:absolute;left:158px;width:884px;font-size:13.5px;line-height:23px;font-weight:300}
.about .btn{position:absolute;left:544px;top:298px;width:112px;height:38px;background:var(--white);color:var(--green);font-size:16px;font-weight:500}

/* footer */
.footer{left:0;top:2824px;width:1200px;height:414px;background:var(--black);color:var(--white)}
.footer h4{position:absolute;font-size:19px;font-weight:400}
.footer .frule{position:absolute;width:34px;height:2px;background:var(--green)}
.footer ul{position:absolute;list-style:none;font-size:13px;line-height:24.6px}
.footer li::before{content:"•";color:var(--green);margin-right:4px}
.flogo{left:551px;top:2927px;width:166px;height:166px;border-radius:50%;border:2px solid var(--white);display:flex;align-items:center;justify-content:center;text-align:center;font-size:20px;font-weight:500;line-height:1.25;color:var(--white)}
.contact{font-size:13px;display:flex;align-items:center;gap:18px;color:var(--white)}
.social{width:37px;height:37px;border-radius:50%;background:var(--white)}
.payment{width:36px;height:28px;background:#d9d9d9;border-radius:3px}
.copy{left:0;top:3238px;width:1200px;height:35px;background:var(--green);color:var(--white);font-size:13px;display:flex;align-items:center;justify-content:center}
</style>
</head>
<body>

<!-- top bar -->
<div class="abs topbar">
  <div class="abs mail">
    <svg width="20" height="16" viewBox="0 0 20 16"><rect x="1" y="1" width="18" height="14" fill="none" stroke="#6a9a5b" stroke-width="1.5"/><path d="M1 1l9 7 9-7" fill="none" stroke="#6a9a5b" stroke-width="1.5"/></svg>
    support@copperlantern.com
  </div>
  <div class="abs links"><a>Home</a><a>FAQs</a><a>Contact Us</a></div>
  <div class="abs icons">
    <span class="ring"><svg width="12" height="11" viewBox="0 0 24 22"><path d="M12 21S2 14 2 7a5 5 0 0 1 10-1 5 5 0 0 1 10 1c0 7-10 14-10 14z" fill="none" stroke="#6a9a5b" stroke-width="2.4"/></svg></span>
    <span class="ring"><svg width="12" height="11" viewBox="0 0 24 22"><path d="M1 2h4l3 12h12l3-9H7" fill="none" stroke="#6a9a5b" stroke-width="2.2"/><circle cx="9" cy="19" r="2" fill="#6a9a5b"/><circle cx="18" cy="19" r="2" fill="#6a9a5b"/></svg></span>
  </div>
</div>

<!-- header -->
<div class="abs brand-dot"></div>
<div class="abs brand">COPPER<small>LANTERN</small></div>
<div class="abs search">Search
  <svg width="18" height="18" viewBox="0 0 20 20"><circle cx="8" cy="8" r="6" fill="none" stroke="#6a9a5b" stroke-width="2"/><path d="M12.5 12.5L18 18" stroke="#6a9a5b" stroke-width="2.2"/></svg>
</div>

<!-- nav -->
<nav class="abs nav"><ul>
  <li>Personalized Gifts</li><li>Home Decor</li><li>Gnome</li><li>Craft Supplies</li><li>Pre-Cut Shapes</li><li>Unfinished Wood</li><li>Personalized Family Tree</li><li>Halloween</li>
</ul></nav>

<!-- hero -->
<section class="abs hero" role="img" aria-label="Laser cut wooden name ornaments with dinosaur engravings on a dark wood table beside pine branches and a red bauble"></section>
<div class="abs hero-ornaments"></div>
<div class="abs hero-copy">
  <h1>Personalized Gifts</h1>
  <h2>For Your Loved One’s</h2>
  <ul><li>• Premium 3.2mm MDF</li><li>• Fast Delivery</li><li>• Personalised Item</li><li>• Unique Design</li><li>• Quality Guaranteed</li></ul>
  <a class="btn">Shop Now</a>
</div>

<!-- categories -->
<h2 class="abs sec-title" style="top:726px">SHOP BY CATEGORIES</h2>
<div class="abs sec-rule" style="top:782px"></div>

<div class="abs cat" style="left:142px;top:806px">
  <svg width="56" height="56" viewBox="0 0 56 56" fill="none" stroke="#222" stroke-width="2"><rect x="4" y="20" width="40" height="10"/><rect x="7" y="30" width="34" height="22"/><path d="M24 20v32M24 20c-6-12-16-8-10-2M24 20c6-12 16-8 10-2"/><rect x="30" y="36" width="20" height="16"/><path d="M40 36v16M30 43h20"/></svg>
  <i class="bar"></i><span>Personalized Gifts</span></div>
<div class="abs cat" style="left:376px;top:806px">
  <svg width="56" height="56" viewBox="0 0 56 56" fill="none" stroke="#222" stroke-width="2"><rect x="6" y="14" width="44" height="38" rx="3"/><rect x="12" y="20" width="32" height="26"/><path d="M12 40l9-9 8 8 6-5 9 8"/><circle cx="34" cy="27" r="3"/><path d="M22 14l6-8 6 8"/></svg>
  <i class="bar"></i><span>Home Decor</span></div>
<div class="abs cat" style="left:613px;top:806px">
  <svg width="56" height="56" viewBox="0 0 56 56" fill="none" stroke="#222" stroke-width="2"><path d="M4 26L16 6l12 20zM30 30l11-18 11 18z"/><path d="M8 26v18c0 6 16 6 16 0V26M34 30v14c0 5 14 5 14 0V30"/></svg>
  <i class="bar"></i><span>Gnome</span></div>
<div class="abs cat" style="left:849px;top:806px">
  <svg width="56" height="56" viewBox="0 0 56 56" fill="none" stroke="#222" stroke-width="2"><path d="M28 52S4 36 4 18a12 12 0 0 1 24-4 12 12 0 0 1 24 4c0 18-24 34-24 34z"/></svg>
  <i class="bar"></i><span>Craft Supplies</span></div>

<div class="abs cat" style="left:142px;top:996px">
  <svg width="56" height="56" viewBox="0 0 56 56" fill="none" stroke="#222" stroke-width="2"><path d="M20 4h32v32H36M4 20h32v32H4z"/><path d="M14 28v-4h4M26 24h4v4M30 40v4h-4M18 44h-4v-4" stroke-width="1.6"/></svg>
  <i class="bar"></i><span>Pre-Cut Shapes</span></div>
<div class="abs cat" style="left:376px;top:996px">
  <svg width="56" height="56" viewBox="0 0 56 56" fill="none" stroke="#222" stroke-width="2"><rect x="6" y="4" width="44" height="48"/><path d="M18 4c-6 14 8 20 0 48M32 4c-4 10 10 14 6 28s-2 20 2 20M44 4c-4 8 6 10 6 16"/></svg>
  <i class="bar"></i><span>Unfinished Wood</span></div>
<div class="abs cat" style="left:613px;top:996px">
  <svg width="56" height="56" viewBox="0 0 56 56" fill="none" stroke="#222" stroke-width="2"><circle cx="28" cy="10" r="6"/><circle cx="14" cy="20" r="6"/><circle cx="42" cy="20" r="6"/><circle cx="14" cy="36" r="6"/><circle cx="42" cy="36" r="6"/><circle cx="28" cy="28" r="6"/><path d="M28 34v18M14 52h28"/></svg>
  <i class="bar"></i><span>Personalized Family Tree</span></div>
<div class="abs cat" style="left:849px;top:996px">
  <svg width="56" height="56" viewBox="0 0 56 56" fill="none" stroke="#222" stroke-width="2"><ellipse cx="28" cy="32" rx="22" ry="19"/><path d="M28 13c0-6 4-9 8-9"/><path d="M17 28l5-4 3 5zM39 28l-5-4-3 5zM16 38c6 6 18 6 24 0"/></svg>
  <i class="bar"></i><span>Halloween</span></div>

<!-- featured -->
<h2 class="abs sec-title" style="top:1248px">FEATURED PROUCTS</h2>
<div class="abs sec-rule" style="top:1304px"></div>

<div class="abs tab on" style="left:222px;width:84px">All</div>
<div class="abs tab" style="left:329px;width:126px">New Arrivals</div>
<div class="abs tab" style="left:478px;width:185px">Personalized Family Tree</div>
<div class="abs tab" style="left:686px;width:141px">Best Selling</div>
<div class="abs tab" style="left:849px;width:127px">Top Rated</div>

<div class="abs card" style="left:142px;top:1413px">
  <div class="ph" role="img" aria-label="Wooden shiplap family tree sign with script lettering" style="background:linear-gradient(135deg,#8a6a4c,#d8cbb4 50%,#7a5a3e)"></div>
  <h3>Faux Shiplap Personalized<br>Family Tree</h3>
  <div class="acts"><span class="ring">♡</span><span class="ring"></span></div>
  <div class="price">$69.00</div></div>
<div class="abs card" style="left:452px;top:1413px">
  <div class="ph" role="img" aria-label="Framed camper wall sign hanging on a pale blue wall beside ferns" style="background:linear-gradient(90deg,#8bb07a,#c9dde6 35%,#2a2a2a 55%,#c9dde6 85%)"></div>
  <div class="badge">NEW</div>
  <h3>Camping Wall Decor, RV Hanging,<br>Family Name Sign for Outdoors,</h3>
  <div class="acts"><span class="ring">♡</span><span class="ring"></span></div>
  <div class="price">$75.00</div></div>
<div class="abs card" style="left:760px;top:1413px">
  <div class="ph" role="img" aria-label="Wooden family ornament with hanging mitten tags on a rustic table" style="background:linear-gradient(135deg,#7a1e1e,#6b4a34 40%,#d8c2a0 60%,#6b4a34)"></div>
  <h3>Custom Family Christmas<br>Ornament – Mittens</h3>
  <div class="acts"><span class="ring">♡</span><span class="ring"></span></div>
  <div class="price">$17.00 – $26.00</div></div>

<div class="abs card" style="left:142px;top:1753px">
  <div class="ph" role="img" aria-label="Round wooden pet memorial ornament with paw print and wings" style="background:radial-gradient(circle at 50% 50%,#e6d3cf 30%,#8a5e55 75%)"></div>
  <h3>In Memory of Lost Pet<br>Ornament</h3>
  <div class="acts"><span class="ring">♡</span><span class="ring"></span></div>
  <div class="price">$16.00</div></div>
<div class="abs card" style="left:452px;top:1753px">
  <div class="ph" role="img" aria-label="Glowing laser cut pumpkin lantern with small pumpkins on a dark table" style="background:linear-gradient(135deg,#1a1a1a,#3a2e28 45%,#f0a040 60%,#2a2420)"></div>
  <h3>, Laser Cut Pumpkin, Laser Engrave,<br>Pumpkin, Halloween Decorations</h3>
  <div class="acts"><span class="ring">♡</span><span class="ring"></span></div>
  <div class="price">$24.00</div></div>
<div class="abs card" style="left:760px;top:1753px">
  <div class="ph" role="img" aria-label="Unfinished blank wooden gnome cutout on a grey wood surface" style="background:linear-gradient(135deg,#5a5856,#d8d2c8 45%,#6a6866)"></div>
  <div class="badge">NEW</div>
  <h3>Ufinished Blank Interchangeable<br>Gnome Wooden Sign, DIY Gnome Decor</h3>
  <div class="acts"><span class="ring">♡</span><span class="ring"></span></div>
  <div class="price">$36.00</div></div>

<a class="abs btn" style="left:492px;top:2097px;width:112px;height:36px;font-size:17px">Shop Now</a>
<a class="abs btn" style="left:620px;top:2097px;width:113px;height:36px;font-size:17px;background:var(--grey-btn)">View All</a>

<!-- coupon -->
<div class="abs coupon"></div>
<svg class="abs coupon-dark" width="222" height="113" viewBox="0 0 222 113"><path d="M56 0H220l-4 6 4 6-4 6 4 6-4 6 4 6-4 6 4 6-4 6 4 6-4 6 4 6-4 6 4 6-4 6 4 6-4 6 4 7H56A56 56 0 0 1 56 0z" fill="#000"/></svg>
<div class="abs coupon-text">
  <div><span class="get">GET </span><span class="pct">10%</span><span class="off"> OFF</span></div>
  <div class="sub">YOUR FIRST ORDER!</div>
</div>
<div class="abs field" style="left:543px;width:169px"><svg width="12" height="12" viewBox="0 0 12 12"><circle cx="6" cy="3.5" r="3" fill="#6a9a5b"/><path d="M0 12a6 5 0 0 1 12 0z" fill="#6a9a5b"/></svg>Your Name*</div>
<div class="abs field" style="left:722px;width:172px"><svg width="12" height="12" viewBox="0 0 12 12"><circle cx="6" cy="3.5" r="3" fill="#6a9a5b"/><path d="M0 12a6 5 0 0 1 12 0z" fill="#6a9a5b"/></svg>Your Email Address*</div>
<a class="abs btn" style="left:639px;top:2295px;width:156px;height:32px;font-size:16px">Get Coupon</a>

<!-- about -->
<section class="abs about">
  <h2>About Elsa Hartwig</h2>
  <p style="top:140px">Lorem ipsum dolor sit amet, consectetuer adipiscing elit, sed diam nonummy nibh euismod tincidunt ut laoreet dolore magna aliquam erat volutpat. Ut wisi enim ad minim veniam, quis nostrud exerci tation ullamcorper suscipit lobortis nisl ut aliquip ex ea commodo conser in hendrerit in vulputate velit esse molestie consequat, vel illum dolore eu feugiat nulla facilisis at vero.</p>
  <p style="top:217px">Lorem ipsum dolor sit amet, consectetuer adipiscing elit, sed diam nonummy nibh euismod tincidunt ut laoreet dolore magna aliquam erat volutpat. Ut wisi enim ad minim veniam, quis nostrud exerci tation ullamcorper suscipit lobortis nisl ut aliquip ex ea commodo conser in hendrerit in vulputate velit esse molestie consequat, vel illum dolore eu feugiat nulla facilisis at vero.</p>
  <a class="btn">Shop Now</a>
</section>

<!-- footer -->
<footer class="abs footer">
  <h4 style="left:142px;top:82px">Quick Links</h4>
  <i class="frule" style="left:142px;top:116px"></i>
  <ul style="left:142px;top:126px"><li>Personalized Gifts</li><li>Home Decor</li><li>Gnome</li><li>Craft Supplies</li><li>Pre-Cut Shapes</li><li>Unfinished Wood</li></ul>
  <ul style="left:327px;top:126px"><li>Personalized Family Tree</li><li>Halloween</li><li>FAQs</li><li>Contact Us</li><li>Terms &amp; Condition</li></ul>

  <h4 style="left:776px;top:82px">Contact Details</h4>
  <i class="frule" style="left:776px;top:116px"></i>
  <div class="abs contact" style="left:776px;top:130px">
    <svg width="18" height="24" viewBox="0 0 18 24"><path d="M9 23S1 13 1 8a8 8 0 0 1 16 0c0 5-8 15-8 15z" fill="none" stroke="#6a9a5b" stroke-width="1.6"/><circle cx="9" cy="8" r="3" fill="none" stroke="#6a9a5b" stroke-width="1.6"/></svg>
    <span>Maple Ridge, OR 97001</span></div>
  <div class="abs contact" style="left:776px;top:178px;gap:14px">
    <svg width="20" height="20" viewBox="0 0 24 24"><path d="M5 2l4 5-2 3c1 3 4 6 7 7l3-2 5 4-3 4C10 22 2 14 1 5z" fill="none" stroke="#6a9a5b" stroke-width="1.6"/></svg>
    <span>+41 (0) 55 210 48 17</span></div>
  <div class="abs" style="left:776px;top:212px;font-size:11px;line-height:14px;width:270px">Please reach out to us if you have any questions or concerns.</div>
  <div class="abs contact" style="left:776px;top:246px;gap:14px">
    <svg width="20" height="18" viewBox="0 0 20 16"><rect x="1" y="1" width="18" height="14" fill="none" stroke="#6a9a5b" stroke-width="1.5"/><path d="M1 1l9 7 9-7" fill="none" stroke="#6a9a5b" stroke-width="1.5"/></svg>
    <span>support@copperlantern.com</span></div>

  <div class="abs" style="left:285px;top:343px;font-size:14px">Follow Us On</div>
  <div class="abs" style="left:383px;top:333px;display:flex;gap:9px"><i class="social"></i><i class="social"></i><i class="social"></i><i class="social"></i></div>
  <i class="abs" style="left:604px;top:322px;width:1px;height:52px;background:#555"></i>
  <div class="abs" style="left:635px;top:343px;font-size:14px">We Accept</div>
  <div class="abs" style="left:722px;top:337px;display:flex;gap:10px"><i class="payment"></i><i class="payment"></i><i class="payment"></i><i class="payment"></i></div>
</footer>
<div class="abs flogo">COPPER<br>LANTERN</div>
<div class="abs copy">Copyright © 2022 Copper Lantern. All Rights Reserved</div>

</body>
</html>
```